依頼詳細
■入れてほしい文言
エクセルデータ参照してください

■ のぼり、ポスターサイズ情報
サイズ:横600mm×縦1800mm以内

■ デザインへの要望
洋風調、和風調 のぼりデザインを作成したい
デザイン参考に添付ファイルの画像を参照
記載項目
サイズ:横600mm×縦1800mm以内
希望イメージ
シンプル 複雑
単色 カラフル
暗い 明るい
日常 高級
遊び心 厳粛
未来的 伝統的
女性的 男性的
希望する色
納品ファイル
• イラストレーター形式 (.ai)
• フォトショップ形式 (.psd)
• PNG形式 (.png)
補足説明

```html
<!DOCTYPE html>
<html lang="ja">
<head>
<meta charset="utf-8">
<title>越後の小京都 のぼり</title>
<link rel="stylesheet" href="https://fonts.googleapis.com/css2?family=Kaisei+Decol:wght@700&family=Noto+Sans+JP:wght@700&display=swap">
<style>
  :root {
    --page: #ffffff;
    --wood-light: #f4e6dc;
    --wood-mid: #d9b7a2;
    --wood-dark: #a87a62;
    --brown: #4a200c;
    --crimson: #8e1c26;
    --ink-light: #ffffff;
  }
  html, body {
    margin: 0;
    padding: 0;
    width: 849px;
    height: 1200px;
    overflow: hidden;
    background: var(--page);
  }
  .canvas {
    position: relative;
    width: 849px;
    height: 1200px;
    background: var(--page);
  }
  .banner {
    position: absolute;
    left: 249px;
    top: 108px;
    width: 351px;
    height: 1002px;
    overflow: hidden;
  }
  .banner-art {
    position: absolute;
    inset: 0;
    width: 100%;
    height: 100%;
    display: block;
  }
  .title {
    position: absolute;
    left: 0;
    width: 100%;
    top: 420px;
    margin: 0;
    text-align: center;
    font-family: "Kaisei Decol", serif;
    font-weight: 700;
    font-size: 46px;
    letter-spacing: 1px;
    color: var(--ink-light);
    line-height: 1;
  }
  .emblem {
    position: absolute;
    left: 162px;
    top: 498px;
    width: 22px;
    height: 22px;
    border: 2px solid var(--ink-light);
    border-radius: 50%;
    box-sizing: border-box;
  }
  .org-name {
    position: absolute;
    left: 0;
    width: 100%;
    top: 538px;
    margin: 0;
    text-align: center;
    font-family: "Noto Sans JP", sans-serif;
    font-weight: 700;
    font-size: 25px;
    letter-spacing: 2px;
    color: var(--ink-light);
    line-height: 1;
  }
</style>
</head>
<body>
<div class="canvas">
  <div class="banner">
    <svg class="banner-art" viewBox="0 0 351 1002" xmlns="http://www.w3.org/2000/svg">
      <defs>
        <linearGradient id="woodTop" x1="0" y1="0" x2="1" y2="1">
          <stop offset="0" stop-color="var(--wood-light)"/>
          <stop offset="0.5" stop-color="var(--wood-mid)"/>
          <stop offset="1" stop-color="var(--wood-dark)"/>
        </linearGradient>
        <linearGradient id="woodBottom" x1="0" y1="0" x2="1" y2="1">
          <stop offset="0" stop-color="var(--wood-dark)"/>
          <stop offset="0.45" stop-color="var(--wood-mid)"/>
          <stop offset="1" stop-color="var(--wood-light)"/>
        </linearGradient>
      </defs>
      <g class="kumiko-top" role="img" aria-label="木組み細工の格子模様の写真">
        <polygon points="0,0 351,0 351,230 0,341" fill="url(#woodTop)"/>
      </g>
      <g class="kumiko-bottom" role="img" aria-label="麻の葉模様の組子細工の写真">
        <polygon points="0,600 351,520 351,1002 0,1002" fill="url(#woodBottom)"/>
      </g>
      <polygon class="band-brown" points="0,341 351,230 351,500 0,420" fill="var(--brown)"/>
      <polygon class="band-crimson" points="0,420 351,500 351,520 0,640" fill="var(--crimson)"/>
    </svg>
    <h1 class="title">越後の小京都</h1>
    <span class="emblem" aria-hidden="true"></span>
    <p class="org-name">川辺建具組合</p>
  </div>
</div>
</body>
</html>
```